Lumora Dwellings

Design a stylish Business card- we would like a businness card design that suits plastic business cards. Our card needs to show that we are tech savy and technology based so the design is crucial.

Target Market(s)

22-40

Industry/Entity Type

Plastic

Requirements
Must have
• attached is our logo. also double sided card would be nice.
my details

Tobias Fenwright
Director
0471596234
www.lumoradwellings.com.au
17 Ashcombe Lane, West Perth

```html
<!DOCTYPE html>
<html lang="en">
<head>
<meta charset="utf-8">
<title>Lumora Dwellings – Business Card</title>
<link rel="stylesheet" href="https://fonts.googleapis.com/css2?family=Noto+Sans:wght@400;700&display=swap">
<style>
  :root {
    --backdrop: #eedd14;
    --card-dark: #17191c;
    --card-mid: #2c4a54;
    --brand-teal: #3a9fbd;
    --card-light: #ffffff;
    --ink: #111111;
  }
  * { box-sizing: border-box; margin: 0; padding: 0; }
  html, body { width: 1200px; height: 922px; overflow: hidden; }
  body {
    background: var(--backdrop);
    font-family: "Noto Sans", Verdana, sans-serif;
    position: relative;
  }
  .card {
    position: absolute;
    left: 329px;
    width: 582px;
    height: 356px;
    border-radius: 27px;
    overflow: hidden;
  }
  .card--front {
    top: 77px;
    background: linear-gradient(90deg, var(--card-dark) 0%, #24343a 28%, var(--card-mid) 46%, #1f2d33 70%, var(--card-dark) 100%);
  }
  .card__lens { position: absolute; inset: 0; }
  .front-brand {
    position: absolute;
    left: 0; right: 0; top: 158px;
    text-align: center;
  }
  .brand-name {
    display: inline-flex;
    align-items: center;
    gap: 12px;
    color: var(--brand-teal);
    font-weight: 700;
    text-transform: uppercase;
    letter-spacing: 2px;
  }
  .brand-name__mark {
    width: 30px; height: 30px;
    border: 3px solid var(--brand-teal);
    border-radius: 4px;
  }
  .front-brand .brand-name { font-size: 40px; }

  .card--back {
    top: 451px;
    background: var(--card-light);
  }
  .back-brand {
    position: absolute;
    left: 53px; top: 50px;
  }
  .back-brand .brand-name { font-size: 22px; gap: 8px; letter-spacing: 1px; }
  .back-brand .brand-name__mark { width: 18px; height: 18px; border-width: 2px; }

  .contact {
    position: absolute;
    left: 53px; top: 201px;
    color: var(--ink);
    font-size: 19px;
    line-height: 21.8px;
    font-style: normal;
  }
  .contact__name { font-weight: 700; }
</style>
</head>
<body>
  <section class="card card--front" aria-label="Card front">
    <svg class="card__lens" viewBox="0 0 582 356" width="582" height="356" aria-hidden="true">
      <defs>
        <linearGradient id="lensFill" x1="0" y1="0" x2="1" y2="0">
          <stop offset="0" stop-color="#2fb8dc" stop-opacity="0.9"/>
          <stop offset="0.35" stop-color="#3b6f7e" stop-opacity="0.75"/>
          <stop offset="1" stop-color="#2a4a55" stop-opacity="0.6"/>
        </linearGradient>
      </defs>
      <path d="M282 0 C220 80 215 260 260 356 L262 356 C360 270 395 90 286 0 Z" fill="url(#lensFill)"/>
      <path d="M282 0 C220 80 215 260 260 356" fill="none" stroke="#4fd0ef" stroke-width="3" opacity="0.7"/>
    </svg>
    <div class="front-brand">
      <span class="brand-name"><span class="brand-name__mark"></span>Lumora Dwellings</span>
    </div>
  </section>

  <section class="card card--back" aria-label="Card back">
    <div class="back-brand">
      <span class="brand-name"><span class="brand-name__mark"></span>Lumora Dwellings</span>
    </div>
    <address class="contact">
      <div class="contact__name">Tobias Fenwright</div>
      <div>Director</div>
      <div>M:0471596234</div>
      <div>W:www.lumoradwellings.com.au</div>
      <div>17 Ashcombe Lane,</div>
      <div>West Perth</div>
    </address>
  </section>
</body>
</html>
```